4x6 Postcard Design Full Color Double Sided

Hello, I am in need of a postcard design. The document with details is attached. And I am writing here also:

To My Dear Colleague,

This week, I want you to do yourself and me a favor, okay?

I want you to ask your boss for a $100,000 per year salary increase. If the answer is no then I want you to “give yourself” a

$10,000 per month pay increase RIGHT NOW!

The opportunity to make 6-7 figures using SIMPLE online systems is exploding right before your eyes. Why aren’t you paying attention? Is It because you don’t have any idea how to earn money online? Or are you intimidated by the thought of it because you’re not tech-savvy?

Throw any negative thoughts out of your mind and let us help you build a $100,000 + yearly income that runs on automatic. We’re not promising a million dollars overnight or that you’ll be able to quit your job tomorrow, BUT if an extra $10,000 per month would help you reach your goals, then you should take action today!

OUR SIMPLE IS SO EASY TO USE, A FIFTH GRADER COULD BE SUCCESSFUL!

We’re so sure you will be successful with our system that we are inviting you to
GET STARTED TODAY FOR FREE!!!

That’s right…for FREE! No credit card is required.

GO SIGN UP NOW:
www.qmvhub.com/joinFREE
Enter Referral ID#

LK-R7859

Free offer expires in 48 hours!!!

Instructions for designers:
I’d like the color scheme to stay consistent with my company’s color scheme. To see the color scheme of Blue Harbor Gain go to www.qmvhub.com
As you are reading the text, please make certain parts of the text be emphasized on the postcard – wherever you feel necessary. When you read it, what would catch your attention? Those parts are the parts I’d like you to emphasize on the card by making them bolder, or a different color, or larger or highlighted.

The postcard is a 4x6 card, double-sided, full color

The text above is for the front side. The back will be the same thing, except in the spot where I have LK-R7859. On the backside it should say: (Use ID# on reverse side)

It’s like you are really only designing a one-sided card because the back side is almost an exact duplicate.

Thank you, you rock! =)

Target Market(s)

work from home seekers / make money online enthusiasts

Font styles to use
Serif

Requirements
Must have
• Color scheme similar to the color scheme at www.qmvhub.com
• The rest of the requirements are attached to the word doc.
• I will also send the logo, but it wouldn't let me upload because the file is too large.
Nice to have
• I really I am looking for something that really looks clean, but attention-grabbing

```html
<!DOCTYPE html>
<html lang="en">
<head>
<meta charset="utf-8">
<title>Blue Harbor Gain Postcard</title>
<link rel="stylesheet" href="https://fonts.googleapis.com/css2?family=Lato:wght@400;700;900&family=Open+Sans:wght@400;600;700&display=swap">
<style>
  :root{
    --stage:#6d6d6d;
    --card:#ffffff;
    --blue:#5ab4d8;
    --blue-light:#a9dcf0;
    --blue-deep:#2f8fbd;
    --ink:#1d1d1d;
    --grey:#555c63;
    --red:#d3212b;
    --white:#ffffff;
  }
  *{box-sizing:border-box;margin:0;padding:0}
  html,body{width:1200px;height:1200px;overflow:hidden;background:var(--stage)}
  .stage{position:relative;width:1200px;height:1200px}
  .postcard{position:absolute;left:210px;width:780px;height:520px;background:var(--card);overflow:hidden;box-shadow:0 6px 18px rgba(0,0,0,.25)}
  .postcard--front{top:50px}
  .postcard--back{top:630px}

  /* front */
  .front-art{position:absolute;inset:0}
  .brand{position:absolute;left:36px;top:30px;height:44px;display:flex;align-items:center;gap:10px;font-family:"Lato",sans-serif;font-weight:900;font-size:32px;line-height:1;color:var(--grey);letter-spacing:-.5px}
  .brand__dot{width:22px;height:22px;border-radius:50%;background:var(--blue)}
  .greeting{position:absolute;left:36px;top:86px;width:310px;font-family:"Lato",sans-serif;font-weight:700;font-size:28px;line-height:1.2;color:var(--blue);padding-bottom:4px;border-bottom:3px solid var(--blue)}
  .letter{position:absolute;left:36px;top:140px;width:330px;font-family:"Lato",sans-serif;font-weight:700;font-size:15.5px;line-height:1.3;color:var(--ink)}
  .letter p+p{margin-top:10px}
  .pill{position:absolute;left:40px;top:264px;width:330px;height:104px;border-radius:52px;background:var(--blue);color:var(--white);text-align:center;font-family:"Open Sans",sans-serif;padding-top:8px}
  .pill__amount{font-size:36px;font-weight:700;line-height:1.05}
  .pill__line{font-size:19px;line-height:1.2}
  .pill__now{font-size:24px;font-weight:600;line-height:1.1}
  .referral{position:absolute;font-family:"Lato",sans-serif;border-top:1.5px dashed #444;border-bottom:1.5px dashed #444;padding:5px 4px}
  .referral__id{font-weight:700;color:var(--ink);line-height:1.2}
  .referral__expires{font-weight:900;color:var(--red);line-height:1.2}
  .signup{position:absolute;text-align:center;font-family:"Open Sans",sans-serif}
  .signup__label{color:var(--ink);letter-spacing:.5px;line-height:1.3}
  .signup__url{color:var(--blue);font-weight:600;line-height:1.3}
  .front .referral{left:40px;top:378px;width:330px}
  .front .referral__id{font-size:21px}
  .front .referral__expires{font-size:18px}
  .front .signup{left:40px;top:448px;width:330px}
  .front .signup__label{font-size:15px}
  .front .signup__url{font-size:21px}

  /* back */
  .copy-block{position:absolute;left:0;width:560px;background:var(--blue);color:var(--white);font-family:"Open Sans",sans-serif}
  .copy-block--top{top:0;height:208px;padding:14px 20px 0 22px;font-size:12.5px;line-height:1.42}
  .copy-block--top p+p{margin-top:8px}
  .headline{position:absolute;left:0;top:208px;width:560px;height:58px;padding:6px 22px;font-family:"Open Sans",sans-serif;font-weight:700;font-size:18px;line-height:1.25;color:var(--blue-deep)}
  .headline__line{display:block}
  .headline__line--full{text-align:justify;text-align-last:justify}
  .copy-block--bottom{top:266px;height:104px;padding:10px 22px;font-size:14px;line-height:1.35}
  .copy-block__cta{display:block;margin-top:6px;font-family:"Lato",sans-serif;font-size:19px;font-weight:700;color:var(--red)}
  .copy-block__note{font-weight:600}
  .back .referral{left:36px;top:378px;width:500px;text-align:center}
  .back .referral__id{font-size:24px}
  .back .referral__expires{font-size:21px}
  .back .signup{left:36px;top:452px;width:500px}
  .back .signup__label{font-size:18px}
  .back .signup__url{font-size:26px}
  .stamp-box{position:absolute;left:690px;top:34px;width:58px;height:66px;border:1.5px solid #222}
  .address-line{position:absolute;left:595px;width:160px;border-top:1.5px solid #222}
</style>
</head>
<body>
<main class="stage">

  <section class="postcard postcard--front front" aria-label="Postcard front">
    <svg class="front-art" width="780" height="520" viewBox="0 0 780 520">
      <defs>
        <linearGradient id="photoTone" x1="0" y1="0" x2="1" y2="1">
          <stop offset="0" stop-color="#e3f1f8"/>
          <stop offset="1" stop-color="#f7fbfd"/>
        </linearGradient>
      </defs>
      <circle cx="705" cy="180" r="316" fill="none" stroke="var(--blue-light)" stroke-width="16"/>
      <circle cx="705" cy="180" r="305" fill="none" stroke="var(--blue)" stroke-width="6"/>
      <circle cx="705" cy="180" r="300" fill="url(#photoTone)" role="img" aria-label="Photo of a smiling businessman in a white shirt with arms crossed"/>
      <path d="M340 232 q30 4 12 28" fill="none" stroke="var(--red)" stroke-width="2"/>
      <path d="M352 260 l-1 -11 M352 260 l9 -6" fill="none" stroke="var(--red)" stroke-width="2"/>
    </svg>
    <div class="brand"><span class="brand__dot"></span>Blue Harbor Gain</div>
    <h1 class="greeting">To My Dear Colleague,</h1>
    <div class="letter">
      <p>This week, I want you to do yourself and me a favor, okay?</p>
      <p>I want you to ask your boss for a $100,000 per year salary increase. If the answer is no then I want you to “give yourself” a</p>
    </div>
    <div class="pill">
      <div class="pill__amount">$10,000</div>
      <div class="pill__line">per month pay increase</div>
      <div class="pill__now">RIGHT NOW!</div>
    </div>
    <div class="referral">
      <div class="referral__id">Enter Referral ID# LK-R7859</div>
      <div class="referral__expires">Free offer expires in 48 hours!!!</div>
    </div>
    <div class="signup">
      <div class="signup__label">GO SIGN UP NOW:</div>
      <div class="signup__url">www.qmvhub.com/joinFREE</div>
    </div>
  </section>

  <section class="postcard postcard--back back" aria-label="Postcard back">
    <div class="copy-block copy-block--top">
      <p>The opportunity to make 6-7 figures using SIMPLE online systems is exploding right before your eyes. Why aren’t you paying attention? Is It because you don’t have any idea how to earn money online? Or are you intimidated by the thought of it because you’re not tech-savvy?</p>
      <p>Let us help you build a $100,000 + yearly income that runs on automatic. We’re not promising a million dollars overnight or that you’ll be able to quit your job tomorrow, BUT if an extra $10,000 per month would help you reach your goals, then you should take action today!</p>
    </div>
    <h2 class="headline"><span class="headline__line headline__line--full">OUR SIMPLE IS SO EASY TO USE, A FIFTH</span><span class="headline__line">GRADER COULD BE SUCCESSFUL!</span></h2>
    <div class="copy-block copy-block--bottom">
      We’re so sure you will be successful with our system that we are inviting you to
      <span class="copy-block__cta">GET STARTED TODAY FOR FREE!!!</span>
      <span class="copy-block__note">That’s right…for FREE! No credit card is required.</span>
    </div>
    <div class="referral">
      <div class="referral__id">Enter Referral ID# LK-R7859</div>
      <div class="referral__expires">Free offer expires in 48 hours!!!</div>
    </div>
    <div class="signup">
      <div class="signup__label">GO SIGN UP NOW:</div>
      <div class="signup__url">www.qmvhub.com/joinFREE</div>
    </div>
    <div class="stamp-box"></div>
    <div class="address-line" style="top:340px"></div>
    <div class="address-line" style="top:378px"></div>
    <div class="address-line" style="top:416px"></div>
  </section>

</main>
</body>
</html>
```